Brambleway Gardening Services. A6 flyer single sided

Need an A6 flyer designing. Single sided.
I am a gardener.
I do lawn mowing - one-off garden tidy ups or regular fortnightly visits.
All kinds of trees expertly felled, topped or pruned.
Hedge cutting.
Fencing replaced or repaired.
Fully insured.
Access to fully qualified and licenced tree arborist
07741 206319 or 01632 470918.

I have attached my business card and letter head logo.
I'm open to new designs without incorporating any of my artwork.

Industry/Entity Type

Gardener

```html
<!DOCTYPE html>
<html lang="en">
<head>
<meta charset="utf-8">
<title>Brambleway Gardening Services – A6 Flyer</title>
<link href="https://fonts.googleapis.com/css2?family=Noto+Sans:wght@700;800&display=swap" rel="stylesheet">
<style>
  :root {
    --band-black: #000000;
    --grass-dark: #17300f;
    --grass-mid: #2a4f1c;
    --grass-light: #3b6627;
    --text-white: #ffffff;
    --service-green: #a9c93c;
    --text-shadow: rgba(0, 0, 0, 0.55);
  }
  html, body {
    margin: 0;
    padding: 0;
    width: 1200px;
    height: 851px;
    overflow: hidden;
    background: var(--band-black);
  }
  .flyer {
    position: relative;
    width: 1200px;
    height: 851px;
    background: var(--band-black);
    font-family: "Noto Sans", Verdana, sans-serif;
    font-weight: 700;
    color: var(--text-white);
    text-align: center;
  }
  .lawn-photo {
    position: absolute;
    left: 0;
    top: 52px;
    width: 1200px;
    height: 745px;
    background:
      radial-gradient(ellipse at 50% 45%, var(--grass-light) 0%, var(--grass-mid) 45%, var(--grass-dark) 100%);
  }
  .content {
    position: absolute;
    left: 0;
    top: 0;
    width: 1200px;
    text-shadow: 0 2px 4px var(--text-shadow);
  }
  .content p, .content h1, .content h2 { margin: 0; position: absolute; left: 0; width: 1214px; }
  .brand-name {
    top: 220px;
    font-size: 68px;
    font-weight: 800;
    letter-spacing: 4px;
    line-height: 80px;
  }
  .tagline {
    top: 308px;
    font-size: 30px;
    letter-spacing: 3.6px;
    line-height: 40px;
  }
  .services {
    position: absolute;
    top: 368px;
    left: 0;
    width: 1214px;
    margin: 0;
    padding: 0;
    list-style: none;
    color: var(--service-green);
    font-size: 24px;
    line-height: 36px;
    letter-spacing: 2.2px;
  }
  .contact-name {
    top: 566px;
    font-size: 37px;
    line-height: 46px;
    letter-spacing: 3px;
  }
  .phone {
    font-size: 31px;
    line-height: 40px;
    letter-spacing: 4.5px;
  }
  .phone-mobile { top: 620px; }
  .phone-landline { top: 668px; }
  .email {
    top: 718px;
    font-size: 30px;
    line-height: 40px;
    letter-spacing: 1.5px;
  }
</style>
</head>
<body>
  <main class="flyer">
    <div class="lawn-photo" role="img" aria-label="Photograph of a lawn seen from above with gardening tools laid on the grass: a mower, hedge trimmer, trowel, loppers, rake, strimmer, long-handled hoe and a red glove"></div>
    <div class="content">
      <h1 class="brand-name">BRAMBLEWAY</h1>
      <h2 class="tagline">GARDENING SERVICES &amp; TREE WORK</h2>
      <ul class="services">
        <li>Regular Fortnightly Visits or 1 Off Garden Tidy-Ups</li>
        <li>Lawn Mowing &amp; Hedge Cutting</li>
        <li>All Trees Expertly Felled, Topped or Pruned</li>
        <li>Fencing Replaced or Repaired</li>
        <li>Fully Insured - Access to a Licensed Tree Arborist</li>
      </ul>
      <p class="contact-name">Rob Carrow</p>
      <p class="phone phone-mobile">07741 206319</p>
      <p class="phone phone-landline">01632 470918</p>
      <p class="email">brambleway.garden@postmail.net</p>
    </div>
  </main>
</body>
</html>
```